A Military/Intel consulting firm needs a web design.

We are a niche consulting business that specializes in assisting customers get business with the Military and Intelligence agencies.

Accelerate Growth
Accelerate Time to Market
Focused Acceleration
A GROWING TEAM OF INNOVATIVE, TENACIOUS THINKERS WHO THRIVE ON SOLVING COMPLICATED PROBLEMS.
Intelligence Based Due Diligence

Target Market(s)

Technology, engineering, Unmanned Aerial Vehicle (UAV) companies and satellite operators

Industry/Entity Type

Information Technology

Coding

Coded - Design and coding required

Number of Pages Required

3 page

Requirements
Must have
• We are consultants that identify small companies that can use our services to sell in to mainly Northern Readiness Bureau or US intelligence agency.
Nice to have
• I like the feel of this site: http://kelvoranet.com/
Should not have
• None come to mind

```html
<!DOCTYPE html>
<html lang="en">
<head>
<meta charset="utf-8">
<title>Halvern Group — Field Intelligence Consultants</title>
<link href="https://fonts.googleapis.com/css2?family=Jura:wght@500;600&family=Open+Sans:wght@400;600;700&display=swap" rel="stylesheet">
<style>
:root{
  --navy:#0b3c73;
  --blue:#0d5aa8;
  --footer:#06315f;
  --footer-line:#1d4a7a;
  --ink:#333;
  --muted:#8a8a8a;
  --band:#f5f5f5;
  --white:#fff;
}
*{box-sizing:border-box;margin:0;padding:0}
html,body{width:1200px;height:2542px;overflow:hidden}
body{position:relative;background:var(--white);font-family:"Open Sans",Arial,sans-serif;color:var(--ink)}
.abs{position:absolute}
.display{font-family:"Jura","Open Sans",sans-serif;font-weight:600}

/* nav */
.site-nav{left:0;top:0;width:1200px;height:81px;background:linear-gradient(#1569bd,#0a4c92 60%,#073a73)}
.site-nav a{position:absolute;top:0;height:81px;line-height:78px;color:var(--white);text-decoration:none;font-size:18.5px;transform:translateX(-50%)}
.nav-sep{position:absolute;top:0;width:1px;height:81px;background:rgba(255,255,255,.18)}

/* brand */
.brand{left:0;top:81px;width:1200px;height:182px;text-align:center}
.brand-mark{position:absolute;left:560px;top:18px;width:80px;height:80px;border-radius:50%;background:#b3c3d9}
.brand-name{position:absolute;left:0;width:1200px;top:118px;font-weight:700;font-size:21px;color:var(--navy);letter-spacing:.2px}
.brand-tag{position:absolute;left:0;width:1200px;top:148px;font-size:9.5px;color:var(--navy)}

/* hero */
.hero{left:0;top:263px;width:1200px;height:498px;background:
  radial-gradient(ellipse 380px 300px at 500px 230px,rgba(120,112,96,.55),transparent 70%),
  radial-gradient(ellipse 260px 260px at 860px 260px,rgba(95,95,92,.5),transparent 70%),
  linear-gradient(90deg,#2b2b2b 0%,#454543 35%,#3a3a38 65%,#2a2a29 100%)}
.hero-list{position:absolute;left:100px;top:192px;list-style:none}
.hero-list li{position:relative;padding-left:30px;height:42.5px;font-family:"Jura",sans-serif;font-weight:500;font-size:23px;color:var(--white)}
.hero-list svg{position:absolute;left:0;top:7px}
.hero-dots{position:absolute;top:446px;left:562px}
.hero-dots span{display:inline-block;width:14px;height:14px;border-radius:50%;background:#8d8d8d;margin-right:17px}
.hero-dots span.on{background:var(--white)}

/* shared section text */
.section-title{left:0;width:1200px;text-align:center;font-size:29px;color:#222}
.section-title b{font-weight:600;color:var(--navy)}
.lead{left:170px;width:860px;text-align:center;font-size:15.5px;line-height:25px;color:#444}
.btn{display:block;background:linear-gradient(#1765b3,#0a447f);color:var(--white);text-decoration:none;border-radius:3px;text-align:center;font-size:15px;border:1px solid #06325f}

/* services */
.services{left:0;top:1029px;width:1200px;height:356px;background:var(--band)}
.service{position:absolute;top:42px;width:320px;text-align:center}
.service-icon{display:block;margin:0 auto;width:108px;height:108px;border-radius:50%;background:linear-gradient(#1466b5,#072f5d)}
.service-icon svg{display:block}
.service h3{margin-top:28px;font-family:"Jura",sans-serif;font-weight:600;font-size:24px;color:var(--navy)}
.service p{margin:18px auto 0;width:290px;font-size:12.5px;line-height:20.5px;color:#444}

/* quote band */
.quote-band{left:0;top:1385px;width:1200px;height:263px;background:
  radial-gradient(ellipse 300px 160px at 880px 150px,rgba(110,115,140,.45),transparent 70%),
  linear-gradient(90deg,#3e3d3b 0%,#5a5753 45%,#4d4b4a 70%,#3b3a39 100%)}
.quote-mark{position:absolute;left:98px;top:88px;font-family:Georgia,serif;font-weight:700;font-size:72px;line-height:60px;color:var(--white)}
.quote-text{position:absolute;left:173px;top:104px;width:920px;font-size:11.8px;line-height:15px;color:var(--white)}
.quote-author{position:absolute;left:170px;top:157px;font-size:12.5px;color:var(--white)}

/* discretion */
.photo-frame{left:98px;top:1839px;width:449px;height:271px;background:var(--white);padding:7px;box-shadow:0 2px 8px rgba(0,0,0,.3)}
.photo{width:100%;height:100%;background:linear-gradient(90deg,#2c3d5e 0%,#6a7e9c 45%,#c9d3dd 100%)}
.copy{left:570px;top:1832px;width:530px;font-size:12px;line-height:20.5px;color:var(--muted)}
.copy p+p{margin-top:17px}

/* footer */
.site-footer{left:0;top:2166px;width:1200px;height:376px;background:var(--footer)}
.footer-title{position:absolute;top:52px;font-family:"Jura",sans-serif;font-weight:600;font-size:20px;color:var(--white)}
.social{position:absolute;left:100px;top:95px}
.social span{display:inline-block;width:22px;height:22px;border-radius:2px;margin-right:5px}
.news-item{position:absolute;left:334px;width:300px}
.news-thumb{position:absolute;left:0;top:0;width:93px;height:78px;background:#2e6aa6;padding:7px}
.news-thumb div{width:100%;height:100%;background:linear-gradient(135deg,#c7ccd2,#6c7684)}
.news-item h4{position:absolute;left:107px;top:4px;font-size:16px;font-weight:700;color:var(--white);white-space:nowrap}
.news-item time{position:absolute;left:107px;top:33px;font-size:11.5px;color:var(--white)}
.quick-links{position:absolute;left:659px;top:101px;list-style:none}
.quick-links li{font-size:12.5px;line-height:20.7px;color:var(--white)}
.contact{position:absolute;left:866px;top:101px;width:240px;font-size:12.5px;line-height:20.5px;color:var(--white)}
.footer-rule{position:absolute;left:0;top:314px;width:1200px;height:1px;background:var(--footer-line)}
.copyright{position:absolute;left:0;width:1200px;top:336px;text-align:center;font-size:12px;color:var(--white)}
</style>
</head>
<body>

<nav class="abs site-nav">
  <a href="#" style="left:266px">Home</a>
  <span class="nav-sep" style="left:325px"></span>
  <a href="#" style="left:380px">About</a>
  <span class="nav-sep" style="left:442px"></span>
  <a href="#" style="left:524px">Procurement</a>
  <span class="nav-sep" style="left:612px"></span>
  <a href="#" style="left:671px">Clients</a>
  <span class="nav-sep" style="left:732px"></span>
  <a href="#" style="left:797px">Projects</a>
  <span class="nav-sep" style="left:863px"></span>
  <a href="#" style="left:922px">Contact</a>
</nav>

<header class="abs brand">
  <span class="brand-mark"></span>
  <div class="brand-name">HALVERN GROUP</div>
  <div class="brand-tag">Field Intelligence Consultants</div>
</header>

<section class="abs hero" role="img" aria-label="Photograph of two soldiers in helmets and tactical gear, in muted greyscale">
  <ul class="hero-list">
    <li><svg width="14" height="18" viewBox="0 0 14 18"><path d="M3 2l8 7-8 7" fill="none" stroke="#fff" stroke-width="3.5"/></svg>Accelerate Growth</li>
    <li><svg width="14" height="18" viewBox="0 0 14 18"><path d="M3 2l8 7-8 7" fill="none" stroke="#fff" stroke-width="3.5"/></svg>Accelerate Time to Market</li>
    <li><svg width="14" height="18" viewBox="0 0 14 18"><path d="M3 2l8 7-8 7" fill="none" stroke="#fff" stroke-width="3.5"/></svg>Focused Acceleration</li>
    <li><svg width="14" height="18" viewBox="0 0 14 18"><path d="M3 2l8 7-8 7" fill="none" stroke="#fff" stroke-width="3.5"/></svg>Intelligence Based Due Diligence</li>
  </ul>
  <div class="hero-dots"><span></span><span class="on"></span><span></span></div>
</section>

<h2 class="abs section-title display" style="top:800px">WELCOME TO <b>HALVERN</b></h2>
<p class="abs lead" style="top:845px">We are consultants that identify small companies that can use our services to sell in to mainly Northern Readiness Bureau or US intelligence agency.</p>
<a class="abs btn" href="#" style="left:544px;top:917px;width:112px;height:49px;line-height:47px">Read More</a>

<section class="abs services">
  <div class="service" style="left:82px">
    <span class="service-icon">
      <svg width="108" height="108" viewBox="0 0 108 108" role="img" aria-label="Briefcase icon">
        <rect x="30" y="42" width="48" height="34" rx="4" fill="#fff"/>
        <path d="M44 42v-6a3 3 0 0 1 3-3h14a3 3 0 0 1 3 3v6" fill="none" stroke="#fff" stroke-width="4"/>
        <rect x="30" y="55" width="48" height="3" fill="#0d4f94"/>
        <rect x="50" y="52" width="8" height="9" rx="1" fill="#0d4f94"/>
      </svg>
    </span>
    <h3>BUSINESS</h3>
    <p>Neque porro quisquam est, qui dolorem ipsum quia dolor sit amet, consectetur, adipisci velit, sed quia non numquam tem.</p>
  </div>
  <div class="service" style="left:440px">
    <span class="service-icon">
      <svg width="108" height="108" viewBox="0 0 108 108" role="img" aria-label="Shield icon">
        <path d="M54 28l22 8v16c0 15-9 24-22 30-13-6-22-15-22-30V36z" fill="#fff"/>
        <path d="M54 42l4 8 9 1-6.5 6 1.7 9L54 61.5 45.8 66l1.7-9-6.5-6 9-1z" fill="#0d4f94"/>
      </svg>
    </span>
    <h3>MILITARY</h3>
    <p>Neque porro quisquam est, qui dolorem ipsum quia dolor sit amet, consectetur, adipisci velit, sed quia non numquam tem.</p>
  </div>
  <div class="service" style="left:801px">
    <span class="service-icon">
      <svg width="108" height="108" viewBox="0 0 108 108" role="img" aria-label="Magnifier icon">
        <circle cx="49" cy="49" r="16" fill="none" stroke="#fff" stroke-width="6"/>
        <path d="M61 61l14 14" stroke="#fff" stroke-width="8" stroke-linecap="round"/>
      </svg>
    </span>
    <h3>INTELLIGENCE</h3>
    <p>Neque porro quisquam est, qui dolorem ipsum quia dolor sit amet, consectetur, adipisci velit, sed quia non numquam tem.</p>
  </div>
</section>

<section class="abs quote-band" role="img" aria-label="Close-up of an eye overlaid with circuit-board graphics">
  <div class="quote-mark">&ldquo;</div>
  <p class="quote-text">Neque porro quisquam est, qui dolorem ipsum quia dolor sit amet, consectetur, adipisci velit, sed quia non numquam eius modi tempora incidunt ut labore et dolore magnam aliquam quaerat voluptatem.</p>
  <div class="quote-author">- John Doe -</div>
</section>

<h2 class="abs section-title display" style="top:1681px">DISCRETION</h2>
<p class="abs lead" style="top:1737px">We are consultants that identify small companies that can use our services to sell in to mainly Northern Readiness Bureau or US intelligence agency.</p>

<div class="abs photo-frame"><div class="photo" role="img" aria-label="Photograph of two businessmen in suits meeting at a table"></div></div>
<div class="abs copy">
  <p>Nemo enim ipsam voluptatem quia voluptas sit aspernatur aut odit aut fugit, sed quia consequuntur magni dolores eos qui ratione voluptatem sequi nesciunt.</p>
  <p>Neque porro quisquam est, qui dolorem ipsum quia dolor sit amet, consectetur, adipisci velit, sed quia non numquam eius modi tempora incidunt ut labore et dolore magnam aliquam quaerat voluptatem. U</p>
</div>
<a class="abs btn" href="#" style="left:570px;top:1983px;width:123px;height:53px;line-height:51px">Read More</a>

<footer class="abs site-footer">
  <h3 class="footer-title" style="left:100px">STAY IN TOUCH</h3>
  <div class="social">
    <span style="background:#2f6fb8"></span><span style="background:#3c9be0"></span><span style="background:#e8912a"></span><span style="background:#d8453a"></span>
  </div>

  <h3 class="footer-title" style="left:331px">LATEST NEWS</h3>
  <div class="news-item" style="top:82px">
    <div class="news-thumb"><div role="img" aria-label="Photo of business people"></div></div>
    <h4>Lorem ipsum dolor</h4>
    <time>Jun 18,2015</time>
  </div>
  <div class="news-item" style="top:202px">
    <div class="news-thumb"><div role="img" aria-label="Photo of a businessman"></div></div>
    <h4>Lorem ipsum dolor</h4>
    <time>Jun 18,2015</time>
  </div>

  <h3 class="footer-title" style="left:656px">QUICK LINKS</h3>
  <ul class="quick-links">
    <li>Home</li><li>About</li><li>Procurement</li><li>Discretion</li><li>Clients</li><li>Products</li><li>Special Projects</li><li>Contact</li>
  </ul>

  <h3 class="footer-title" style="left:864px">CONTACT US</h3>
  <div class="contact">
    <p>Nemo enim ipsam voluptatem quia voluptas sit aspernatur</p>
    <p style="margin-top:20px">1800-555-0192</p>
    <p>info@halvernmail.com</p>
  </div>

  <div class="footer-rule"></div>
  <div class="copyright">&copy; Copyright 2015 Halvern</div>
</footer>

</body>
</html>
```